Fundraising Study Day East of England. Lift the January blues!

A flyer to advertise a fundraising event of lectures for dental hygienists and therapists in support of the exemption campaign. Currently dental hygienists and therapists require a prescription to deliver certain treatment or recommend certain toothpastes. If we are successful in the campaign we will be able to treat patients without these restrictions.

Dental

```html
<!DOCTYPE html>
<html lang="en">
<head>
<meta charset="utf-8">
<title>Fundraising Study Day East of England</title>
<link href="https://fonts.googleapis.com/css2?family=Montserrat:wght@600;700;800&family=Source+Sans+3:ital,wght@0,400;0,600;0,700;1,700&display=swap" rel="stylesheet">
<style>
:root{
  --navy:#2c5585;
  --panel-dark:#2d5888;
  --panel-light:#41719f;
  --teal:#2a8fb3;
  --ink:#1d1d1d;
  --page-bg:#e9e9e9;
  --sheet-top:#ffffff;
  --sheet-bottom:#ececec;
  --white:#ffffff;
}
*{box-sizing:border-box;margin:0;padding:0}
html,body{width:1200px;height:1166px;overflow:hidden;background:var(--page-bg)}
.flyer{position:absolute;left:224px;top:46px;width:756px;height:1060px;display:flex;box-shadow:0 6px 18px rgba(0,0,0,.18)}
.main{width:468px;height:100%;background:linear-gradient(180deg,var(--sheet-top) 0%,var(--sheet-top) 55%,var(--sheet-bottom) 100%);position:relative}
.title{font-family:"Montserrat",sans-serif;font-weight:700;color:var(--navy);text-align:center;font-size:33px;line-height:40px;padding-top:18px;letter-spacing:.2px}
.tagline{font-family:"Montserrat",sans-serif;font-weight:700;color:var(--teal);text-align:center;font-size:19px;line-height:24px}
.hero{position:absolute;left:0;top:131px;width:468px;height:303px;background:linear-gradient(180deg,#a4522d 0%,#c0754a 18%,#93707a 42%,#6f83a8 66%,#b4b8c6 100%)}
.intro{position:absolute;left:17px;top:452px;width:440px;font-family:"Source Sans 3",sans-serif;font-size:13.4px;line-height:16.7px;color:var(--ink)}
.agenda-title{position:absolute;left:17px;top:540px;font-family:"Montserrat",sans-serif;font-weight:700;font-size:29px;color:var(--navy)}
.agenda{position:absolute;left:19px;top:580px;width:442px;list-style:none;font-family:"Source Sans 3",sans-serif;font-size:13.5px;line-height:16.9px;color:var(--ink)}
.agenda li{position:relative;padding-left:20px}
.agenda li::before{content:"";position:absolute;left:6px;top:10px;bottom:-4px;border-left:1px dashed var(--navy)}
.agenda li:last-child::before{bottom:0}
.slot{display:block;font-weight:700;color:var(--navy);position:relative}
.slot::before{content:"";position:absolute;left:-20px;top:3px;width:11px;height:11px;border:2px solid var(--navy);border-radius:50%;background:var(--white)}
.slot.pause{font-style:italic}
.booking{position:absolute;left:17px;top:972px;font-family:"Montserrat",sans-serif}
.booking h2{font-size:16.5px;font-weight:700;color:var(--navy);letter-spacing:.6px}
.booking p{font-family:"Source Sans 3",sans-serif;font-weight:600;font-size:13.5px;line-height:18px;color:var(--ink);margin-top:2px;width:430px;word-break:break-all}
.details{width:288px;height:100%;background:linear-gradient(90deg,var(--panel-dark) 0%,var(--panel-light) 55%,var(--panel-dark) 100%);position:relative;color:var(--white);font-family:"Montserrat",sans-serif;font-weight:700;text-align:center}
.icon{position:absolute;left:84px;width:120px;height:120px;border:3px solid var(--white);border-radius:50%;display:flex;align-items:center;justify-content:center}
.detail-text{position:absolute;left:0;width:100%;font-size:22px;line-height:29px}
</style>
</head>
<body>
<article class="flyer">
  <section class="main">
    <h1 class="title">Fundraising Study Day<br>East of England.</h1>
    <p class="tagline">Lift the January blues!</p>
    <div class="hero" role="img" aria-label="Photo of a speaker at a lectern facing a full lecture hall audience"></div>
    <p class="intro">A fundraising event to support our exemptions project. The day will consist of a series of presentations ranging from the new ECPD to new technologies. The aim, being to enhance our learning and raise funds to support the exemptions campaign. The speaker line includes some of the UK and Irelands most respected dental professionals in our field.</p>
    <h2 class="agenda-title">Agenda</h2>
    <ul class="agenda">
      <li><span class="slot">9.30 - 10.15</span>Helen Marsh: Immediate past president of the NADH will be updating us on all things ECPD</li>
      <li><span class="slot">10.15 - 11.00</span>Megan Carlow: Will provide an update on teeth whiteing and explain how social media has impacted her business<br>Juliet Rowan: Our internationally acclaimed speaker will update our knowledge of periodontal disease and nutrition and new technologies.</li>
      <li><span class="slot pause">11.00 - 11.30 &nbsp;Break</span></li>
      <li><span class="slot">11.30 - 13.00</span>Sinead Kerrigan &amp; Melanie Pryce: Will be providing a combined presentation on 'Scaling your business' and start to finish ultrasonic scaler techniques. The aim being to build our business with effective communications, systems and protocols. This sessions promises audience participation!</li>
      <li><span class="slot pause">12.00 - 14.00 lunch</span></li>
      <li><span class="slot">14.00 - 15.00</span>Priya Patel: Save your back. All things posture.</li>
      <li><span class="slot pause">15.00 - 15.30 Break</span></li>
      <li><span class="slot">15.30 -16.30</span>Juliet Rowan: Our internationally acclaimed speaker will update our knowledge of periodontal disease and nutrition and new technologies.</li>
    </ul>
    <div class="booking">
      <h2>BOOK YOUR TICKETS HERE</h2>
      <p>https://www.ticketsdesk.example/e/fundraising-study-day-east-of-england-lift-the-january-blues-tickets-40218836</p>
    </div>
  </section>
  <aside class="details">
    <div class="icon" style="top:82px">
      <svg width="60" height="80" viewBox="0 0 60 80"><path d="M30 78 C18 58 4 44 4 28 A26 26 0 0 1 56 28 C56 44 42 58 30 78Z" fill="#fff"/><circle cx="30" cy="27" r="9" fill="#3a6a99"/></svg>
    </div>
    <p class="detail-text" style="top:218px">Larchfield Hotel<br>Oak Way, Elmby<br>EL4 7QT</p>
    <div class="icon" style="top:350px">
      <svg width="76" height="64" viewBox="0 0 76 64" fill="none" stroke="#fff" stroke-width="3"><rect x="2" y="8" width="72" height="54" rx="6"/><rect x="14" y="2" width="8" height="10" fill="#3a6a99"/><rect x="54" y="2" width="8" height="10" fill="#3a6a99"/><g stroke-width="2"><rect x="8" y="20" width="18" height="10"/><rect x="29" y="20" width="18" height="10"/><rect x="50" y="20" width="18" height="10"/><rect x="8" y="33" width="18" height="10"/><rect x="29" y="33" width="18" height="10"/><rect x="50" y="33" width="18" height="10" fill="#fff"/><rect x="8" y="46" width="18" height="10"/><rect x="29" y="46" width="18" height="10"/><rect x="50" y="46" width="18" height="10"/></g></svg>
    </div>
    <p class="detail-text" style="top:486px">Friday<br>19 January 2018</p>
    <div class="icon" style="top:598px">
      <svg width="80" height="80" viewBox="0 0 80 80" fill="none" stroke="#fff"><circle cx="40" cy="40" r="34" stroke-width="7"/><path d="M40 18 V42 L54 52" stroke-width="6" stroke-linecap="round"/></svg>
    </div>
    <p class="detail-text" style="top:734px;font-size:23px">09:00 – 16:30 (GMT)</p>
    <div class="icon" style="top:809px">
      <svg width="78" height="78" viewBox="0 0 78 78" fill="none" stroke="#fff" stroke-width="3"><path d="M50 6 L72 6 L72 28 L32 70 L8 46 Z" stroke-linejoin="round"/><circle cx="62" cy="16" r="4"/><text x="34" y="48" fill="#fff" stroke="none" font-family="Montserrat,sans-serif" font-size="26" font-weight="700" transform="rotate(-45 38 42)" text-anchor="middle">$</text></svg>
    </div>
    <p class="detail-text" style="top:946px">£101.48 Only</p>
  </aside>
</article>
</body>
</html>
```